New Business Card Design Project

I need a clean, professional business card. I'd like it to have some color, but not be wild. We do technology consulting and we have clients large and small who trust us with some of their most important data and projects. Simple but not boring should drive all design proposals. Multicolored and two sided, but with a matte finish, I think.
For more on tone, check out our website: http://brindlequay.com

Target Market(s)

Upper management of respected businesses. Tech savvy, but not "hipster".

Industry/Entity Type

Business

Requirements
Must have
• Files need to be provided in .eps and in .pdf in a manner that allows for easy updates.
Must have Name, Title, Phone, Email, Twitter, Website
Nice to have
• Logo/Name shouldn't be too big. One thing I've read several places is that the bigger the logo, the smaller the brand. A good article on dos and don'ts here: http://www.mossvane.com/2011/02/business-card-experience.html

```html
<!DOCTYPE html>
<html lang="en">
<head>
<meta charset="utf-8">
<title>Brindle Quay business card</title>
<link rel="stylesheet" href="https://fonts.googleapis.com/css2?family=Michroma&family=Montserrat:wght@400;600&display=swap">
<style>
  :root {
    --backdrop: #ece9e4;
    --card: #ffffff;
    --teal: #3a8fa3;
    --green: #8aab3a;
    --ink: #555a5e;
    --ink-dark: #2e3133;
    --grey-band: #808285;
  }
  * { box-sizing: border-box; margin: 0; padding: 0; }
  html, body { width: 1200px; height: 702px; overflow: hidden; }
  body {
    background: var(--backdrop);
    font-family: "Montserrat", sans-serif;
    position: relative;
  }
  .card {
    position: absolute;
    top: 196px;
    width: 540px;
    height: 310px;
    background: var(--card);
    border-radius: 28px;
    overflow: hidden;
    box-shadow: 0 6px 18px rgba(0,0,0,0.18);
  }
  .card--front { left: 40px; }
  .card--back { left: 620px; }

  .name-accent {
    position: absolute; left: 0; top: 42px;
    width: 14px; height: 46px; background: var(--teal);
  }
  .holder-name {
    position: absolute; left: 32px; top: 40px;
    font-weight: 600; font-size: 19px; color: var(--teal);
  }
  .holder-title {
    position: absolute; left: 32px; top: 66px;
    font-size: 13px; font-weight: 400; color: var(--green);
  }
  .brand {
    position: absolute; right: 36px; top: 78px;
    display: flex; align-items: center; gap: 10px;
  }
  .brand-dot { width: 14px; height: 14px; border-radius: 50%; background: var(--teal); }
  .brand-name {
    font-size: 24px; font-weight: 400; letter-spacing: 1px; color: var(--ink);
    text-transform: uppercase;
  }
  .contacts {
    position: absolute; left: 40px; top: 150px;
    list-style: none; font-size: 13px; color: var(--ink-dark);
  }
  .contacts li { display: flex; align-items: center; gap: 8px; height: 28px; }
  .contacts svg { width: 12px; height: 12px; flex: none; }

  .footer-band {
    position: absolute; left: 0; right: 0; bottom: 0; height: 40px;
    background: var(--teal);
    border-top: 6px solid var(--grey-band);
  }
  .band-url {
    position: absolute; left: 40px; bottom: 12px;
    font-family: "Michroma", sans-serif; font-size: 11px; letter-spacing: 3px;
    color: #ffffff;
  }

  .back-brand {
    position: absolute; left: 0; right: 0; top: 110px;
    display: flex; justify-content: center; align-items: center; gap: 16px;
  }
  .back-brand .brand-dot { width: 26px; height: 26px; }
  .back-brand .brand-name { font-size: 34px; }
  .back-url {
    position: absolute; left: 0; right: 0; bottom: 40px; text-align: center;
    font-family: "Michroma", sans-serif; font-size: 14px; letter-spacing: 4px;
    color: var(--ink-dark);
  }
</style>
</head>
<body>
  <section class="card card--front">
    <div class="name-accent"></div>
    <h1 class="holder-name">Your Name</h1>
    <p class="holder-title">Title</p>
    <div class="brand">
      <span class="brand-dot"></span>
      <span class="brand-name">Brindle Quay</span>
    </div>
    <ul class="contacts">
      <li>
        <svg viewBox="0 0 12 12" aria-hidden="true"><path d="M3 1 L5 3.5 L4 5 C4.8 6.6 5.6 7.4 7 8 L8.5 7 L11 9 L9.5 11 C5 10.5 1.5 7 1 2.5 Z" fill="var(--teal)"/></svg>
        <span>0123 456780</span>
      </li>
      <li>
        <svg viewBox="0 0 12 12" aria-hidden="true"><rect x="1" y="3" width="10" height="7" fill="var(--teal)"/><path d="M1 3 L6 7 L11 3" stroke="#fff" stroke-width="1" fill="none"/></svg>
        <span>info@brindlequay.com</span>
      </li>
      <li>
        <svg viewBox="0 0 12 12" aria-hidden="true"><rect x="1" y="1" width="10" height="10" rx="2" fill="var(--teal)"/></svg>
        <span>@brindlequay</span>
      </li>
    </ul>
    <div class="footer-band"></div>
    <p class="band-url">www.brindlequay.com</p>
  </section>

  <section class="card card--back">
    <div class="back-brand">
      <span class="brand-dot"></span>
      <span class="brand-name">Brindle Quay</span>
    </div>
    <p class="back-url">www.brindlequay.com</p>
  </section>
</body>
</html>
```